Business card and (possibly) logo

Hi - we need a new business card.
We have an existing logo that we quite like but we are open to options.
We are an architectural firm - we specialize in upmarket residential work and apartment blocks.
We are chasing a business card at present but also want to extensively update our website going forward to attract a much higher level of client / investor / developer.
Our current logo is black, grey and yellow and based on the sun/moon temples in Mexico.
We are open to variations.
We want to communicate professionalism, trust, quality.
Our website is www.corvelldesignhouse.com.au - but note as above - we want to change the website as well to be a lot 'classier' and to appeal to a higher end market.

thanks

Target Market(s)

We are an architect firm - our target market is Developers and builders of high end houses and luxury apartment blocks. Also private home owners wanting to build excellent expensive houses. (ideally over $1m budgets)

Industry/Entity Type

Residential

Requirements
Must have
• Logo
Contact details;
Name
phone, mobile, email, web

```html
<!DOCTYPE html>
<html lang="en">
<head>
<meta charset="utf-8">
<title>Corvell Design House — Business Card</title>
<link rel="stylesheet" href="https://fonts.googleapis.com/css2?family=Open+Sans:wght@400;600;700&display=swap">
<style>
  :root {
    --card-bg: #ffffff;
    --brand-grey: #8c8c8c;
    --text-grey: #6f6f6f;
    --brand-orange: #f5a11c;
    --base-band: #050505;
    --chip: #9a9a9a;
  }
  * { margin: 0; padding: 0; box-sizing: border-box; }
  html, body {
    width: 1200px; height: 734px; overflow: hidden;
    background: var(--card-bg);
    font-family: "Open Sans", Arial, sans-serif;
  }
  .card { position: relative; width: 1200px; height: 734px; background: var(--card-bg); }

  .brand {
    position: absolute; left: 0; top: 150px; width: 1200px;
    display: flex; flex-direction: column; align-items: center; gap: 34px;
  }
  .brand__mark {
    width: 120px; height: 120px; border-radius: 50%;
    background: var(--brand-orange);
  }
  .brand__name {
    font-weight: 600; font-size: 58px; letter-spacing: 1px;
    color: var(--brand-grey); line-height: 1;
  }

  .contact { position: absolute; left: 93px; top: 562px; }
  .contact__label { font-size: 31px; color: var(--text-grey); line-height: 1.2; }
  .contact__phone {
    margin-top: 8px; font-weight: 700; font-size: 50px;
    color: var(--brand-orange); letter-spacing: 1px; line-height: 1.1;
  }

  .social { position: absolute; left: 798px; top: 562px; }
  .social__label { font-size: 31px; color: var(--text-grey); line-height: 1.2; }
  .social__list { display: flex; gap: 14px; margin-top: 10px; list-style: none; }
  .social__item { display: flex; flex-direction: column; align-items: center; gap: 4px; width: 74px; }
  .social__chip { width: 62px; height: 62px; background: var(--chip); }
  .social__name { font-size: 13px; color: var(--text-grey); line-height: 1; }

  .base-band {
    position: absolute; left: 0; bottom: 0; width: 1200px; height: 38px;
    background: var(--base-band);
  }
</style>
</head>
<body>
  <main class="card">
    <header class="brand">
      <div class="brand__mark" aria-hidden="true"></div>
      <h1 class="brand__name">CORVELL DESIGN HOUSE</h1>
    </header>

    <section class="contact">
      <p class="contact__label">Call us now on:</p>
      <p class="contact__phone">1300 62 18 45</p>
    </section>

    <section class="social">
      <p class="social__label">Find us on:</p>
      <ul class="social__list">
        <li class="social__item"><span class="social__chip"></span><span class="social__name">Friendly</span></li>
        <li class="social__item"><span class="social__chip"></span><span class="social__name">Chirpline</span></li>
        <li class="social__item"><span class="social__chip"></span><span class="social__name">Reelcast</span></li>
        <li class="social__item"><span class="social__chip"></span><span class="social__name">Linkwork</span></li>
      </ul>
    </section>

    <div class="base-band"></div>
  </main>
</body>
</html>
```